【サイト概要】
可愛くリノベーションした物件を紹介し、入居者を募集する賃貸物件紹介サイトです。
物件紹介だけではなく、周辺の町情報(カフェや雑貨店など)や、暮らしに役立つ情報(収納術や簡単レシピなど)も共に発信し、
物件探しだけでなく女性の暮らしを不動産屋の視点からサポート・応援をするサイトとなります。

【ターゲット】
・主に女性
・部屋探しをしている方
・20代~40代の可愛いものが好きな方
・日々の暮らしがより可愛くなるよう役立つ情報を集めている方

【重視する点】
・可愛らしいデザインが得意な方
・WEBデザインのトンマナに理解のある方
・アイコンや枠・線などの装飾はSVG形式で配置可能なもの(原則単色であり色を変更しても見劣りしないもの)
・PhotoshopまたはXDでデザイン可能な方

【参考サイト】
可愛いの範囲が曖昧になってしまうため、
幾つか参考サイトをピックアップしました。
すべてを兼ね備えたものではなく、
制作者様のお得意なジャンルの“可愛い”に絞っていただきデザインいただければと思います。

▼ナチュラル(北欧風)
https://tenori-kobako.jp/
https://www.mimosoire.jp/
https://www2.torvasu.co.jp/healthcare/pickup/zadankai/
https://www.plum-kitchen.com/

▼ポップ
https://www.sorao.ac.jp/girls/
https://www.mofurin-dots.com/
https://www.harvolin.jp/concert/
https://kumorine-hiraso.or.jp/

▼エレガント
http://tipsvelo.com/
http://rozu-bridal.jp/
https://lumiroe.jp/

【素材について】
Googleドライブに格納しております。
https://files.kamitoru.jp/drive/folders/8KpeRtzXa4LmNoQvBc2YhWsUdFjGiEHxL?usp=sharing
・写真
・イラスト
・見出しの英語サブタイトルなどにはGoogle Fontsから使用可
・アイコンには、Awesomeフォント(Free)やGoogle iconも使用可

※ドライブに格納している素材写真ですが物件や記事の写真にお使いください。
その他必要な写真素材がありましたら、一旦フリー素材や有料レンポジサイトのウォーターマーク入りの仮素材にて作成ください。最終差し替え作業は当方にて行うため不要です。
※イラスト素材についてはこちらで用意できたものを格納しておりますが、使用の有無はお任せいたします。

【デザイン作成に際しご留意いただきたい点】
フォント及びフォントサイズについてはワイヤーのものは参考とせず、作成いただくデザインに準じたフォント及びサイズの選定・規定をお願いいたします。
Googleフォントの使用を想定していますので、システムフォントを使用する箇所についてのフォント選定の参考としてください。

【トンマナのルール化】
WordPressにて実装いたしますので、色味や要素の大きさなど、デザインから色や形の使用ルールが見えるデザインをお願いしたいです。

その他何かご不明な点がございましたら、お気軽にご質問下さい。
よろしくお願いいたします。
赤系、黄・オレンジ系、茶系、線やアイコンの色を変えても使用可能なデザインを希望しています
XDデータでも可
期間が短かったため、ゆとりを持ってご提案いただけるように締め切りを延長いたしました。
少しでもご興味を持っていただけましたら、是非ご応募ください。
良いご縁がありますことを願っております。
とても良いご提案を数件頂いておりますので、
さらに期間を延長させていただいて検討したいと思います。

・社員全員とも相談をし多数決で決定いたしました
・ベース色を変えたときにも利用しやすそうだった

多くの皆様からかわいいご提案を頂きまして、本当にありがとうございました。
すべての方をご当選できればよいのですが、1名となってしまいますこと何卒ご了承ください。
ご提案頂きました9名の皆様には、改めましてお礼申し上げます。
本当にありがとうございました。

```html
<!DOCTYPE html>
<html lang="ja">
<head>
<meta charset="utf-8">
<title>ひだまりのおうち</title>
<link href="https://fonts.googleapis.com/css2?family=Zen+Maru+Gothic:wght@400;500;700&family=Quicksand:wght@500;700&display=swap" rel="stylesheet">
<style>
:root{
  --bg:#fbf8f2;
  --cream:#f5eedf;
  --beige:#efe5d2;
  --yellow:#f3c04f;
  --yellow-soft:#fbe6b0;
  --coral:#e8857a;
  --coral-soft:#f8d7d1;
  --brown:#6b5446;
  --brown-light:#a08d80;
  --line:#e6dccb;
  --white:#ffffff;
}
*{box-sizing:border-box;margin:0;padding:0}
html,body{width:1200px;height:2800px;overflow:hidden}
body{background:var(--bg);font-family:"Zen Maru Gothic",sans-serif;color:var(--brown);position:relative}
.en{font-family:"Quicksand",sans-serif}
.photo{display:block;border-radius:6px}

/* header */
.site-header{position:absolute;top:0;left:0;width:1200px;height:130px;background:var(--white)}
.logo{position:absolute;top:22px;left:0;width:1200px;text-align:center;font-size:22px;font-weight:700;letter-spacing:.12em;color:var(--brown)}
.logo::before{content:"";display:inline-block;width:16px;height:16px;border-radius:50%;background:var(--yellow);margin-right:10px;vertical-align:-1px}
.global-nav{position:absolute;top:66px;left:40px;right:40px;display:flex;gap:12px}
.global-nav a{flex:1;display:flex;align-items:center;justify-content:center;gap:8px;height:44px;border-radius:22px;background:var(--cream);font-size:14px;font-weight:500;color:var(--brown);text-decoration:none}
.global-nav a span{width:18px;height:18px;border-radius:50%;background:var(--yellow)}

/* hero */
.hero{position:absolute;top:150px;left:0;width:1200px;height:330px;overflow:hidden}
.hero-track{display:flex;gap:22px;margin-left:-120px}
.hero-card{flex:0 0 238px}
.hero-card .photo{height:230px;border-radius:8px}
.hero-card p{margin-top:12px;font-size:14px;line-height:1.6;font-weight:500}
.hero-dots{position:absolute;top:495px;left:0;width:1200px;display:flex;justify-content:center;gap:10px}
.hero-dots i{width:10px;height:10px;border-radius:50%;background:var(--line)}
.hero-dots i.on{background:var(--yellow)}

/* section heading */
.heading{position:absolute;left:0;width:1200px;text-align:center}
.heading .badge{display:inline-block;padding:6px 14px;border-radius:14px;background:var(--yellow);color:var(--white);font-size:12px;font-weight:700}
.heading h2{margin-top:10px;font-size:30px;font-weight:700;letter-spacing:.12em;display:flex;justify-content:center;align-items:center;gap:12px}

/* property grid */
.new-list{position:absolute;top:630px;left:40px;width:1120px;display:grid;grid-template-columns:repeat(4,1fr);gap:30px 24px}
.prop-card{background:var(--white);border-radius:8px;padding:12px;height:410px;box-shadow:0 2px 8px rgba(160,130,100,.08)}
.prop-card .photo{height:165px}
.prop-card h3{margin-top:12px;font-size:15px;line-height:1.5;color:var(--coral);font-weight:700}
.prop-card .desc{margin-top:8px;font-size:11px;line-height:1.6;color:var(--brown-light)}
.spec{margin-top:10px;font-size:11px;border-top:1px dashed var(--line)}
.spec div{display:flex;justify-content:space-between;padding:5px 0;border-bottom:1px dashed var(--line)}
.spec b{color:var(--coral);font-size:17px}
.prop-card .date{margin-top:6px;text-align:right;font-size:10px;color:var(--brown-light)}
.more-btn{position:absolute;top:1530px;left:500px;width:200px;height:44px;border-radius:22px;border:2px solid var(--yellow);background:var(--white);text-align:center;line-height:40px;font-size:14px;font-weight:700}

/* read section */
.read-area{position:absolute;top:1600px;left:0;width:1200px;height:960px}
.read-area svg.wave{position:absolute;top:0;left:0}
.read-heading{position:absolute;top:50px;left:40px;width:620px;text-align:center}
.read-heading .sub{font-size:12px;color:var(--brown-light)}
.read-heading h2{margin-top:6px;font-size:28px;letter-spacing:.15em}
.articles{position:absolute;top:140px;left:40px;width:620px;display:flex;flex-direction:column;gap:18px}
.article{display:flex;align-items:center;height:140px}
.article .photo{flex:0 0 240px;height:140px}
.article .body{flex:1;background:var(--white);height:112px;margin-left:-20px;border-radius:8px;padding:20px 24px;font-size:14px;line-height:1.7;font-weight:500;position:relative}
.article.rev{flex-direction:row-reverse}
.article.rev .body{margin-left:0;margin-right:-20px}
.article .body small{position:absolute;right:18px;bottom:12px;font-size:10px;color:var(--brown-light)}
.pager{position:absolute;top:940px;left:300px;display:flex;gap:8px}
.pager i{width:26px;height:26px;border-radius:50%;background:var(--white);border:1px solid var(--line);font-style:normal;font-size:11px;text-align:center;line-height:24px}
.pager i.on{background:var(--coral);color:var(--white);border-color:var(--coral)}

/* ranking */
.ranking{position:absolute;top:20px;left:720px;width:440px}
.rank-head{text-align:center}
.rank-head .tag{display:inline-block;padding:5px 12px;background:var(--coral);color:var(--white);font-size:11px;border-radius:4px}
.rank-head h2{display:inline-block;margin-top:8px;padding:8px 22px;background:var(--yellow-soft);border-radius:6px;font-size:20px;letter-spacing:.08em}
.rank-list{margin-top:20px;display:flex;flex-direction:column;gap:12px}
.rank-item{display:flex;gap:14px;background:var(--white);border-radius:8px;padding:10px;height:100px;position:relative}
.rank-item .photo{flex:0 0 120px;height:80px}
.rank-item .num{position:absolute;top:4px;left:4px;width:24px;height:24px;background:var(--coral);color:var(--white);border-radius:4px;font-size:13px;text-align:center;line-height:24px;font-weight:700}
.rank-item h4{font-size:13px;line-height:1.5}
.rank-item p{margin-top:4px;font-size:11px;color:var(--brown-light)}
.rank-item p b{color:var(--coral);font-size:15px}

.category{position:absolute;top:660px;left:720px;width:440px;background:var(--white);border-radius:10px;padding:22px 28px}
.category .sub{text-align:center;font-size:11px;color:var(--brown-light)}
.category h3{text-align:center;font-size:18px;margin-top:4px;letter-spacing:.1em}
.category ul{list-style:none;margin-top:16px;display:grid;grid-template-columns:repeat(3,1fr);gap:14px}
.category li{display:flex;align-items:center;gap:8px;font-size:13px}
.category li span{width:22px;height:22px;border-radius:50%;background:var(--yellow-soft);border:2px solid var(--yellow)}

/* footer */
.site-footer{position:absolute;top:2600px;left:0;width:1200px;height:200px;background:var(--white);border-top:4px solid var(--yellow)}
.footer-logo{position:absolute;top:50px;left:220px;font-size:18px;font-weight:700;letter-spacing:.1em}
.footer-logo::before{content:"";display:inline-block;width:14px;height:14px;border-radius:50%;background:var(--yellow);margin-right:8px}
.footer-info{position:absolute;top:86px;left:220px;font-size:11px;line-height:1.8;color:var(--brown-light)}
.footer-links{position:absolute;top:50px;left:620px;display:flex;gap:60px;font-size:12px;line-height:2}
.copyright{position:absolute;bottom:16px;width:1200px;text-align:center;font-size:10px;color:var(--brown-light)}
</style>
</head>
<body>

<header class="site-header">
  <div class="logo">ひだまりのおうち</div>
  <nav class="global-nav">
    <a href="#"><span></span>タイプから探す</a>
    <a href="#"><span></span>こだわりから探す</a>
    <a href="#"><span></span>間取りから探す</a>
    <a href="#"><span></span>家賃から探す</a>
    <a href="#"><span></span>よくある質問</a>
    <a href="#"><span></span>店舗案内</a>
  </nav>
</header>

<section class="hero">
  <div class="hero-track">
    <div class="hero-card"><div class="photo" role="img" aria-label="窓辺で過ごす女性の写真" style="background:linear-gradient(135deg,#efe3cf,#d9c3a4)"></div><p>コツコツ貯金で目標の100万円達成のコツ</p></div>
    <div class="hero-card"><div class="photo" role="img" aria-label="手料理が並ぶ食卓の写真" style="background:linear-gradient(135deg,#f3e6d2,#d8a886)"></div><p>ひとり暮らしの簡単すぎる作り置き7日分献立で料理上手に</p></div>
    <div class="hero-card"><div class="photo" role="img" aria-label="明るいリビングの写真" style="background:linear-gradient(135deg,#f5efe6,#e0d3c2)"></div><p>新生活にぴったりのお部屋探しのポイント</p></div>
    <div class="hero-card"><div class="photo" role="img" aria-label="カップを持つ女性の写真" style="background:linear-gradient(135deg,#e9ecf0,#c6ccd4)"></div><p>コロナ禍で増えたおうち時間を快適にする方法</p></div>
    <div class="hero-card"><div class="photo" role="img" aria-label="白い壁の部屋の写真" style="background:linear-gradient(135deg,#f4f0ea,#ddd4c8)"></div><p>狭くて収納に困る部屋でも片付く収納術</p></div>
    <div class="hero-card"><div class="photo" role="img" aria-label="雑貨が飾られた棚の写真" style="background:linear-gradient(135deg,#f1e7d8,#cdb79a)"></div><p>週末に巡りたい街の雑貨店めぐり</p></div>
  </div>
</section>
<div class="hero-dots"><i class="on"></i><i></i><i></i><i></i><i></i></div>

<div class="heading" style="top:540px">
  <span class="badge">人気物件が続々登場</span>
  <h2>
    <svg width="30" height="28" viewBox="0 0 30 28"><path d="M3 14 L15 3 L27 14 V26 H3 Z" fill="var(--yellow)"/><rect x="12" y="17" width="6" height="9" fill="#fff"/></svg>
    新着物件
  </h2>
</div>

<section class="new-list">
  <article class="prop-card"><div class="photo" role="img" aria-label="ロフト付きの部屋の写真" style="background:linear-gradient(135deg,#f2ebe2,#c9b29a)"></div><h3>2階角部屋・ロフト付き 水回り綺麗リノベ</h3><p class="desc">日当たりの良い南向きの角部屋。駅から徒歩8分で買い物にも便利です。</p><div class="spec"><div><span>家賃</span><b>78,000円</b></div><div><span>間取り</span><span>1LDK</span></div><div><span>所在地</span><span>緑区みどり町</span></div></div><p class="date">2021.03.01</p></article>
  <article class="prop-card"><div class="photo" role="img" aria-label="明るい洋室の写真" style="background:linear-gradient(135deg,#f5f1ec,#d6c9bb)"></div><h3>2階角部屋・ロフト付き 水回り綺麗リノベ</h3><p class="desc">日当たりの良い南向きの角部屋。駅から徒歩8分で買い物にも便利です。</p><div class="spec"><div><span>家賃</span><b>78,000円</b></div><div><span>間取り</span><span>1LDK</span></div><div><span>所在地</span><span>緑区みどり町</span></div></div><p class="date">2021.03.01</p></article>
  <article class="prop-card"><div class="photo" role="img" aria-label="ピンクの壁の部屋の写真" style="background:linear-gradient(135deg,#f6e4e0,#e3b9b1)"></div><h3>2階角部屋・ロフト付き 水回り綺麗リノベ</h3><p class="desc">日当たりの良い南向きの角部屋。駅から徒歩8分で買い物にも便利です。</p><div class="spec"><div><span>家賃</span><b>78,000円</b></div><div><span>間取り</span><span>1LDK</span></div><div><span>所在地</span><span>緑区みどり町</span></div></div><p class="date">2021.03.01</p></article>
  <article class="prop-card"><div class="photo" role="img" aria-label="ロフト付きの部屋の写真" style="background:linear-gradient(135deg,#f2ebe2,#c9b29a)"></div><h3>2階角部屋・ロフト付き 水回り綺麗リノベ</h3><p class="desc">日当たりの良い南向きの角部屋。駅から徒歩8分で買い物にも便利です。</p><div class="spec"><div><span>家賃</span><b>78,000円</b></div><div><span>間取り</span><span>1LDK</span></div><div><span>所在地</span><span>緑区みどり町</span></div></div><p class="date">2021.03.01</p></article>
  <article class="prop-card"><div class="photo" role="img" aria-label="内装工事中の部屋の写真" style="background:linear-gradient(135deg,#e6e3df,#b9b3ac)"></div><h3>2階角部屋・ロフト付き 水回り綺麗リノベ</h3><p class="desc">日当たりの良い南向きの角部屋。駅から徒歩8分で買い物にも便利です。</p><div class="spec"><div><span>家賃</span><b>78,000円</b></div><div><span>間取り</span><span>1LDK</span></div><div><span>所在地</span><span>緑区みどり町</span></div></div><p class="date">2021.03.01</p></article>
  <article class="prop-card"><div class="photo" role="img" aria-label="ロフト付きの部屋の写真" style="background:linear-gradient(135deg,#f2ebe2,#c9b29a)"></div><h3>2階角部屋・ロフト付き 水回り綺麗リノベ</h3><p class="desc">日当たりの良い南向きの角部屋。駅から徒歩8分で買い物にも便利です。</p><div class="spec"><div><span>家賃</span><b>78,000円</b></div><div><span>間取り</span><span>1LDK</span></div><div><span>所在地</span><span>緑区みどり町</span></div></div><p class="date">2021.03.01</p></article>
  <article class="prop-card"><div class="photo" role="img" aria-label="明るい洋室の写真" style="background:linear-gradient(135deg,#f5f1ec,#d6c9bb)"></div><h3>2階角部屋・ロフト付き 水回り綺麗リノベ</h3><p class="desc">日当たりの良い南向きの角部屋。駅から徒歩8分で買い物にも便利です。</p><div class="spec"><div><span>家賃</span><b>78,000円</b></div><div><span>間取り</span><span>1LDK</span></div><div><span>所在地</span><span>緑区みどり町</span></div></div><p class="date">2021.03.01</p></article>
  <article class="prop-card"><div class="photo" role="img" aria-label="ピンクの壁の部屋の写真" style="background:linear-gradient(135deg,#f6e4e0,#e3b9b1)"></div><h3>2階角部屋・ロフト付き 水回り綺麗リノベ</h3><p class="desc">日当たりの良い南向きの角部屋。駅から徒歩8分で買い物にも便利です。</p><div class="spec"><div><span>家賃</span><b>78,000円</b></div><div><span>間取り</span><span>1LDK</span></div><div><span>所在地</span><span>緑区みどり町</span></div></div><p class="date">2021.03.01</p></article>
</section>
<a class="more-btn" href="#">一覧を見る</a>

<section class="read-area">
  <svg class="wave" width="1200" height="960" viewBox="0 0 1200 960"><path d="M0 40 Q300 0 600 30 T1200 20 V940 Q900 980 600 945 T0 950 Z" fill="var(--beige)"/></svg>

  <div class="read-heading"><p class="sub">お役立ち情報満載の</p><h2>よみもの</h2></div>
  <div class="articles">
    <div class="article"><div class="photo" role="img" aria-label="手料理が並ぶ食卓の写真" style="background:linear-gradient(135deg,#f3e6d2,#d8a886)"></div><div class="body">ひとり暮らしの簡単すぎる作り置き7日分献立で料理上手に<small>2021.03.01</small></div></div>
    <div class="article rev"><div class="photo" role="img" aria-label="カップを持つ女性の写真" style="background:linear-gradient(135deg,#e9ecf0,#c6ccd4)"></div><div class="body">コロナ禍で増えたおうち時間を快適にする方法<small>2021.03.01</small></div></div>
    <div class="article"><div class="photo" role="img" aria-label="手料理が並ぶ食卓の写真" style="background:linear-gradient(135deg,#f3e6d2,#d8a886)"></div><div class="body">ひとり暮らしの簡単すぎる作り置き7日分献立で料理上手に<small>2021.03.01</small></div></div>
    <div class="article rev"><div class="photo" role="img" aria-label="窓辺で過ごす女性の写真" style="background:linear-gradient(135deg,#efe3cf,#d9c3a4)"></div><div class="body">無理なく楽しくコツコツ貯金で目標の100万円達成<small>2021.03.01</small></div></div>
    <div class="article"><div class="photo" role="img" aria-label="手料理が並ぶ食卓の写真" style="background:linear-gradient(135deg,#f3e6d2,#d8a886)"></div><div class="body">ひとり暮らしの簡単すぎる作り置き7日分献立で料理上手に<small>2021.03.01</small></div></div>
  </div>
  <div class="pager"><i class="on">1</i><i>2</i><i>3</i><i>›</i></div>

  <aside class="ranking">
    <div class="rank-head"><span class="tag">いま一番注目されている物件</span><br><h2>人気物件ランキング</h2></div>
    <div class="rank-list">
      <div class="rank-item"><span class="num">1</span><div class="photo" role="img" aria-label="ロフト付きの部屋の写真" style="background:linear-gradient(135deg,#f2ebe2,#c9b29a)"></div><div><h4>2階角部屋・ロフト付き 水回り綺麗リノベ</h4><p>家賃 <b>78,000円</b> / 1LDK</p></div></div>
      <div class="rank-item"><span class="num">2</span><div class="photo" role="img" aria-label="明るい洋室の写真" style="background:linear-gradient(135deg,#f5f1ec,#d6c9bb)"></div><div><h4>2階角部屋・ロフト付き 水回り綺麗リノベ</h4><p>家賃 <b>78,000円</b> / 1LDK</p></div></div>
      <div class="rank-item"><span class="num">3</span><div class="photo" role="img" aria-label="ピンクの壁の部屋の写真" style="background:linear-gradient(135deg,#f6e4e0,#e3b9b1)"></div><div><h4>2階角部屋・ロフト付き 水回り綺麗リノベ</h4><p>家賃 <b>78,000円</b> / 1LDK</p></div></div>
      <div class="rank-item"><span class="num">4</span><div class="photo" role="img" aria-label="ロフト付きの部屋の写真" style="background:linear-gradient(135deg,#f2ebe2,#c9b29a)"></div><div><h4>2階角部屋・ロフト付き 水回り綺麗リノベ</h4><p>家賃 <b>78,000円</b> / 1LDK</p></div></div>
      <div class="rank-item"><span class="num">5</span><div class="photo" role="img" aria-label="明るい洋室の写真" style="background:linear-gradient(135deg,#f5f1ec,#d6c9bb)"></div><div><h4>2階角部屋・ロフト付き 水回り綺麗リノベ</h4><p>家賃 <b>78,000円</b> / 1LDK</p></div></div>
    </div>
  </aside>

  <div class="category">
    <p class="sub">お役立ち情報満載の</p>
    <h3>いろいろな読みもの</h3>
    <ul>
      <li><span></span>暮らす</li>
      <li><span></span>食べる</li>
      <li><span></span>収納する</li>
      <li><span></span>節約する</li>
      <li><span></span>出かける</li>
      <li><span></span>整える</li>
    </ul>
  </div>
</section>

<footer class="site-footer">
  <div class="footer-logo">ひだまりのおうち</div>
  <p class="footer-info">営業時間 10:00〜18:00<br>定休日 水曜日</p>
  <div class="footer-links">
    <ul style="list-style:none"><li>タイプから探す</li><li>こだわりから探す</li><li>間取りから探す</li></ul>
    <ul style="list-style:none"><li>家賃から探す</li><li>よくある質問</li><li>店舗案内</li></ul>
    <ul style="list-style:none"><li>よみもの</li><li>お問い合わせ</li><li>プライバシー</li></ul>
  </div>
  <p class="copyright en">© Hidamari no Ouchi</p>
</footer>

</body>
</html>
```